40% Off Colour And Hair Service Every Monday + Wedneday

A large window poster approx 1m x 1m when installed
The poster should in someway match the look of our website
lumerova.net.au
please refer to our website for selection of images and choose something similar yourself
final print needs to suitable for a large format poster

.
.
.
.
.
.
.
.
.
.
.
.
.

Target Market(s)

people passing the salon

Industry/Entity Type

Hair And Beauty

Colors

Designer to choose colors to be used in the design.

Requirements
Must have
• (the offer) : 40% Off Colour And Hair Services Every Monday & Wednesday
• (image) : in keeping with our website : lumerova.net.au
• Phone Number : 9283 5067
• (disclaimer - small print)
• Offer Not Available During Christmas Period. Offer
• Excludes Keratin and Hair Extensions
• 40% discount apples to full price adult services – cannot be combined with any other discount
Nice to have
• in keeping with feel of our website: lumerova.net.au
• must be bold, eye catching and easily readable
• sophisticated / classy / modern feel .. nothing tacky

```html
<!DOCTYPE html>
<html lang="en">
<head>
<meta charset="utf-8">
<title>Lumerova Salon &amp; Spa – 40% off Monday &amp; Wednesday</title>
<link rel="stylesheet" href="https://fonts.googleapis.com/css2?family=Arimo:wght@700&family=Source+Sans+3:wght@300;400;600;700&display=swap">
<style>
  :root {
    --poster-bg: #ffffff;
    --brand-red: #c41230;
    --ink: #222222;
    --ink-soft: #333333;
    --white: #ffffff;
  }
  * { box-sizing: border-box; margin: 0; padding: 0; }
  html, body {
    width: 1200px;
    height: 1200px;
    overflow: hidden;
    background: var(--poster-bg);
  }
  .poster {
    position: relative;
    width: 1200px;
    height: 1200px;
    background: var(--poster-bg);
    overflow: hidden;
    font-family: "Source Sans 3", Arial, sans-serif;
  }
  .hero-photo {
    position: absolute;
    inset: 0;
    width: 1200px;
    height: 1200px;
  }
  .offer-badge {
    position: absolute;
    inset: 0;
    width: 1200px;
    height: 1200px;
  }
  .offer-badge text {
    font-family: "Arimo", Arial, sans-serif;
    font-weight: 700;
    fill: var(--white);
  }
  .brand {
    position: absolute;
    left: 74px;
    top: 836px;
  }
  .brand-name {
    font-family: "Source Sans 3", Arial, sans-serif;
    font-weight: 700;
    font-size: 96px;
    line-height: 1;
    letter-spacing: -2px;
    color: var(--brand-red);
  }
  .brand-rule {
    width: 470px;
    height: 2px;
    background: #cfcfcf;
    margin: 6px 0 10px;
  }
  .brand-tagline {
    font-weight: 600;
    font-size: 30px;
    line-height: 1;
    letter-spacing: 22px;
    color: var(--ink);
  }
  .call {
    position: absolute;
    left: 72px;
    top: 1010px;
    font-weight: 300;
    font-size: 58px;
    line-height: 1;
    color: var(--ink);
  }
  .terms {
    position: absolute;
    left: 84px;
    top: 1112px;
    width: 440px;
    list-style: none;
    font-size: 15px;
    line-height: 1.3;
    color: var(--ink-soft);
  }
  .terms li {
    position: relative;
    padding-left: 14px;
    margin-bottom: 6px;
  }
  .terms li::before {
    content: "";
    position: absolute;
    left: 0;
    top: 7px;
    width: 5px;
    height: 5px;
    border-radius: 50%;
    background: var(--brand-red);
  }
</style>
</head>
<body>
<main class="poster">
  <svg class="hero-photo" viewBox="0 0 1200 1200" role="img" aria-label="Model with vivid rainbow-coloured hair, bright neon nails, a colourful beaded necklace and a spiked bracelet">
    <defs>
      <linearGradient id="hair-tones" x1="0" y1="0" x2="1" y2="1">
        <stop offset="0" stop-color="#f25aa8"/>
        <stop offset="0.25" stop-color="#5fc8ee"/>
        <stop offset="0.45" stop-color="#f7a23c"/>
        <stop offset="0.6" stop-color="#e9b49a"/>
        <stop offset="1" stop-color="#d99a80"/>
      </linearGradient>
    </defs>
    <path d="M640 0 H1200 V1200 H700 L690 1000 L760 760 L700 520 Z" fill="url(#hair-tones)"/>
  </svg>

  <svg class="offer-badge" viewBox="0 0 1200 1200" aria-label="40% off every Monday and Wednesday">
    <circle cx="325" cy="401" r="288" fill="var(--brand-red)"/>
    <text x="90" y="442" font-size="240" textLength="330" lengthAdjust="spacingAndGlyphs">40</text>
    <text x="424" y="366" font-size="138">%</text>
    <text x="428" y="456" font-size="112" textLength="146" lengthAdjust="spacingAndGlyphs">off</text>
    <text x="330" y="536" font-size="47" text-anchor="middle">Every Monday &amp;</text>
    <text x="330" y="592" font-size="47" text-anchor="middle">Wednesday</text>
  </svg>

  <div class="brand">
    <div class="brand-name">lumerova</div>
    <div class="brand-rule"></div>
    <div class="brand-tagline">salon &amp; spa</div>
  </div>

  <div class="call">Call:9283 5067</div>

  <ul class="terms">
    <li>Offer Not Available During Christmas Period.</li>
    <li>Excludes Keratin and Hair Extensions</li>
    <li>40% discount apples to full price adult services – cannot be combined with any other discount</li>
  </ul>
</main>
</body>
</html>
```